New Design for Brightcoilheat [Zimpla]

Hello, This is my 2nd project here. I need a new web design for www.brightcoilheat.com.au which is one of my clients, and an extremely outdated website. It only has a few links and is fairly straight forward, looking for a more professional, up-to-date looking website. Please note: The website will be made under a zimpla white-label platform, so the design MUST be consistent with this type of platform. Many more projects will be up and coming so the best designers will definitely be selected for future projects.
Thankyou

• Please refer to www.brightcoilheat.com.au to find all the content.

```html
<!DOCTYPE html>
<html lang="en">
<head>
<meta charset="utf-8">
<title>Brightcoilheat – Thermal and Sealing Specialists</title>
<link href="https://fonts.googleapis.com/css2?family=Open+Sans:wght@400;600;700&display=swap" rel="stylesheet">
<style>
:root{
  --ink:#2b2b2b;
  --band:#2d2d2d;
  --page:#e7e7e7;
  --card:#ffffff;
  --muted:#7a7a7a;
  --rule:#dcdcdc;
  --soft:#f3f3f3;
  --accent:#7db343;
  --link:#3a9bd6;
  --brand:#e2e2e2;
}
*{margin:0;padding:0;box-sizing:border-box}
html,body{width:769px;height:1200px;overflow:hidden}
body{background:var(--page);font-family:"Open Sans",Arial,sans-serif;color:var(--ink);position:relative}
.top-band{position:absolute;left:0;top:0;width:769px;height:90px;background:var(--band)}
.brand{position:absolute;left:98px;top:22px;display:flex;align-items:center;gap:8px}
.brand-mark{width:26px;height:26px;background:#8a8a8a}
.brand-name{font-size:19px;font-weight:700;color:var(--brand);letter-spacing:.2px}
.brand-tag{position:absolute;left:132px;top:50px;font-size:9px;color:#b5b5b5}
.main-nav{position:absolute;right:96px;top:60px;display:flex;gap:2px}
.main-nav a{font-size:7.5px;font-weight:700;color:#d8d8d8;text-decoration:none;padding:6px 9px;text-transform:uppercase}
.main-nav a.active{background:#fff;color:var(--ink)}
.sheet{position:absolute;left:96px;top:106px;width:577px;height:905px;background:var(--card);box-shadow:0 0 6px rgba(0,0,0,.12)}
.slider{position:absolute;left:10px;top:10px;width:557px;height:212px;background:linear-gradient(135deg,#3a2f2a,#7a6a5c 40%,#c9c3bc 70%,#4a3c34)}
.slider-arrow{position:absolute;top:96px;width:20px;height:20px;border-radius:50%;background:rgba(255,255,255,.85)}
.slider-arrow svg{display:block}
.slider-arrow.prev{left:-4px}.slider-arrow.next{right:-4px}
.intro{position:absolute;left:18px;top:242px;width:541px;height:56px;background:var(--soft);border:1px solid #e6e6e6;padding:11px 16px;font-size:8.5px;line-height:1.6;color:var(--muted)}
.section-title{position:absolute;left:18px;display:flex;align-items:center;gap:7px;font-size:9px;font-weight:700;color:var(--ink);width:541px}
.section-title::before{content:"";width:8px;height:8px;border-radius:50%;border:2px solid #bdbdbd}
.section-title::after{content:"";flex:1;height:1px;background:var(--rule)}
.bullet-cols{position:absolute;left:30px;width:520px;display:grid;grid-template-columns:repeat(3,1fr);column-gap:12px}
.bullet-cols ul{list-style:none}
.bullet-cols li{font-size:7.5px;color:var(--muted);line-height:15px;padding-left:11px;position:relative}
.bullet-cols li::before{content:"";position:absolute;left:0;top:5px;width:5px;height:5px;background:var(--accent)}
.bullet-cols.tight li{line-height:13.5px}
.bullet-cols.tight li::before{top:4px}
.product-strip{position:absolute;left:18px;top:580px;width:541px;height:115px;background:var(--soft);border:1px solid #e4e4e4}
.product-row{position:absolute;left:32px;top:8px;display:flex;gap:8px}
.product-item{width:88px}
.product-photo{width:88px;height:72px;border:2px solid #fff;box-shadow:0 0 2px rgba(0,0,0,.25)}
.product-item p{font-size:6.5px;color:var(--muted);text-align:center;margin-top:4px;line-height:1.3}
.strip-arrow{position:absolute;top:42px;font-size:14px;color:#9a9a9a}
.strip-arrow.prev{left:10px}.strip-arrow.next{right:10px}
.category-grid{position:absolute;left:56px;top:745px;width:480px;display:grid;grid-template-columns:repeat(4,1fr)}
.category-grid a{font-size:7.5px;color:var(--link);text-decoration:none;line-height:15px}
.footer{position:absolute;left:0;top:1030px;width:769px;height:170px;background:var(--band)}
.footer-info{position:absolute;left:98px;top:18px;font-size:7px;line-height:1.55;color:#a9a9a9}
.footer-info strong{color:#dcdcdc;font-weight:600}
.footer-social{position:absolute;right:100px;top:20px;display:flex;gap:6px}
.footer-social span{width:15px;height:15px;border-radius:50%;background:#555}
.footer-copy{position:absolute;right:100px;top:46px;font-size:6.5px;color:#8d8d8d}
</style>
</head>
<body>
<header class="top-band">
  <div class="brand"><span class="brand-mark"></span><span class="brand-name">Brightcoilheat</span></div>
  <div class="brand-tag">Thermal and Sealing Specialists</div>
  <nav class="main-nav">
    <a class="active" href="#">Home</a><a href="#">About Us</a><a href="#">Product</a><a href="#">Service</a><a href="#">Our Client</a><a href="#">Contact</a>
  </nav>
</header>

<main class="sheet">
  <div class="slider" role="img" aria-label="Mosaic of thermal fabric, gasket and insulation product photos"></div>
  <span class="slider-arrow prev" style="left:4px;top:106px"><svg width="20" height="20"><path d="M12 6l-4 4 4 4" fill="none" stroke="#555" stroke-width="1.6"/></svg></span>
  <span class="slider-arrow next" style="right:4px;top:106px"><svg width="20" height="20"><path d="M8 6l4 4-4 4" fill="none" stroke="#555" stroke-width="1.6"/></svg></span>

  <p class="intro">Brightcoilheat are one of Australia's leading suppliers and manufacturers of thermal fabrics and fabrications. The experience, knowledge and facility to design and fabricate give you the quality Australian made products you demand.</p>

  <h2 class="section-title" style="top:318px">Thermal and Sealing Specialists</h2>
  <div class="bullet-cols" style="top:338px">
    <ul><li>Thermal Fabrics and Fabrications</li><li>High and Low Temperature Insulation</li><li>Furnace / Oven Door Seals</li><li>Welding Blankets and Curtains</li><li>Fabric Expansion Joints</li></ul>
    <ul><li>Boat Exhaust Covers</li><li>Thermal Hoods / Covers</li><li>Acoustic Materials</li><li>Pump and Valve Packings</li><li>Gasket Materials</li></ul>
    <ul><li>Standard and Non-Standard Gaskets</li><li>Boilers Gaskets and Seals</li><li>Spiral Wounds</li><li>Brightseal</li><li>and Lots More</li></ul>
  </div>

  <h2 class="section-title" style="top:432px">Thermal Product available at Brightcoilheat</h2>
  <div class="bullet-cols tight" style="top:452px">
    <ul><li>Ceramic Fibre Tapes, Ropes, Sheets, Blankets &amp; Insulation</li><li>Glass Fibre Tapes, Ropes, Sheets, Blankets &amp; Insulation</li><li>Furnace / Oven Fabricated Tape Seals</li><li>Silica Tapes, Ropes &amp; Sheets</li></ul>
    <ul><li>Boiler Close Up Kits</li><li>Welding Blankets, Curtains &amp; Screens</li><li>Exhaust Thermal / Acoustic Covers</li><li>Thermal Hoods / Covers</li></ul>
    <ul><li>Valve and Thermal Covers</li><li>Thermal Fabrics</li><li>Thermal Fabrications – Custom Specification</li><li>Fabric / Metallic Expansion Joints &amp; Associated Metal Work</li></ul>
  </div>

  <h2 class="section-title" style="top:556px">Product Overview</h2>
  <section class="product-strip">
    <span class="strip-arrow prev">&#8249;</span><span class="strip-arrow next">&#8250;</span>
    <div class="product-row">
      <div class="product-item"><div class="product-photo" role="img" aria-label="Thermal product photo" style="background:linear-gradient(#5a4b42,#9a8a7a)"></div><p>Thermal</p></div>
      <div class="product-item"><div class="product-photo" role="img" aria-label="Fabric expansion joint type DPC photo" style="background:linear-gradient(#c8c3bd,#8d8279)"></div><p>Fabric Expansion Joint Type DPC</p></div>
      <div class="product-item"><div class="product-photo" role="img" aria-label="Boiler close up kit photo" style="background:linear-gradient(#e6e3df,#a9a39b)"></div><p>Boiler Close Up Kit</p></div>
      <div class="product-item"><div class="product-photo" role="img" aria-label="Fabric expansion joint photo" style="background:linear-gradient(#b9b1a8,#6e625a)"></div><p>Fabric Expansion Joint</p></div>
      <div class="product-item"><div class="product-photo" role="img" aria-label="Fabric expansion joint type W photo" style="background:linear-gradient(#d9d3cc,#857a70)"></div><p>Fabric Expansion Joint Type W</p></div>
    </div>
  </section>

  <h2 class="section-title" style="top:720px">Category Product</h2>
  <nav class="category-grid">
    <a href="#">Thermal Tapes</a><a href="#">Sealing Ropes</a><a href="#">Injection Moulded</a><a href="#">Injection Machines</a>
    <a href="#">Fabric Tapes</a><a href="#">Welding Blankets</a><a href="#">Acrylic Sheet</a><a href="#">Hoses</a>
    <a href="#">Glass Panel Rooms</a><a href="#">Injection Machine</a><a href="#">Injection Seal</a><a href="#">Valve Rope</a>
    <a href="#">Glass Panel</a><a href="#">Boiler Covers</a><a href="#">Injection Foam</a><a href="#">Valve Covers</a>
  </nav>
</main>

<footer class="footer">
  <div class="footer-info">
    <strong>Brightcoilheat Pty Ltd</strong><br>
    12 Kestrel Road<br>
    Norvale VIC 3999<br>
    Tel : +61 3 5550 0142<br>
    Email : hello@brightcoilheat.com.au<br>
    Contact : Sales Team – Main Desk
  </div>
  <div class="footer-social"><span></span><span></span><span></span><span></span><span></span></div>
  <div class="footer-copy">Copyright 2013 Brightcoilheat Pty Ltd · Company</div>
</footer>
</body>
</html>
```